Harrowgate Home Works Sales Flyer

We want a sales flyer that outlines our companies strengths with Kitchen & Bath Remodeling. We would like highlight those aspects while also showcasing our ability to do decks and home additions. We want financing packages to be a big part of the flyer.

Target Market(s)

Residential Customers

Requirements
Must have
• Financing options
Highlight Kitchen & bath remodeling
Less subtle is our decks and home additions
Nice to have
• Keep within our logo colors-we are looking for informative flyers that leave homeowners eager to call us after a meeting

```html
<!DOCTYPE html>
<html lang="en">
<head>
<meta charset="utf-8">
<title>Harrowgate Home Works – Kitchen &amp; Bath Remodeling Flyer</title>
<link href="https://fonts.googleapis.com/css2?family=Oswald:wght@300;400;500&family=Open+Sans:wght@400;600&family=Montserrat:wght@500;600&display=swap" rel="stylesheet">
<style>
:root{
  --blue:#1f6fc2;
  --blue-deep:#0f4fa8;
  --blue-bright:#2a8be0;
  --navy:#123f86;
  --grey-band:#e9eaec;
  --ink:#3d4656;
  --paper:#ffffff;
  --bg:#d9d9d9;
}
*{margin:0;padding:0;box-sizing:border-box}
html,body{width:1200px;height:847px;overflow:hidden;background:var(--bg)}
body{position:relative;font-family:"Open Sans",Arial,sans-serif}
.flyer{position:absolute;top:98px;width:496px;height:642px;background:var(--paper);overflow:hidden;box-shadow:0 4px 14px rgba(0,0,0,.25)}
.flyer--front{left:82px}
.flyer--back{left:626px}
.abs{position:absolute}
.photo{position:absolute}

/* front */
.front-hero{left:0;top:0;width:496px;height:233px;background:linear-gradient(120deg,#6b6f78 0%,#c9c4bc 35%,#ece9e4 60%,#f5f4f2 100%)}
.ribbon{left:-40px;top:38px;width:260px;height:30px;background:var(--blue);color:#fff;transform:rotate(-30deg);font:italic 400 14px/30px "Open Sans",sans-serif;text-align:center;letter-spacing:.3px}
.brand{right:18px;top:30px;width:150px;text-align:center;color:var(--blue);font:600 19px/1.1 "Montserrat",sans-serif}
.brand-dot{display:block;width:12px;height:12px;background:var(--blue);margin:0 auto 5px}
.title-band{left:0;top:233px;width:496px;height:51px;background:var(--grey-band);text-align:center;color:var(--blue);font:500 29px/51px "Montserrat",sans-serif;letter-spacing:-.5px}
.service-band{left:0;top:284px;width:496px;height:143px;background:linear-gradient(180deg,var(--blue-deep),var(--blue-bright));color:#fff}
.service-band h2{font:300 16px/1 "Oswald",sans-serif;text-align:center;margin-top:12px;letter-spacing:.2px}
.services{display:flex;justify-content:space-around;padding:0 14px;margin-top:14px}
.service{width:112px;text-align:center}
.service svg{width:46px;height:46px;display:block;margin:0 auto 8px}
.service h3{font:400 9px/1 "Oswald",sans-serif;letter-spacing:.2px;margin-bottom:4px}
.service p{font-size:6.6px;line-height:1.35}
.bath-photo{left:0;top:427px;width:496px;height:215px;background:linear-gradient(100deg,#f3f2ef 0%,#d8d4cc 30%,#5c5f63 55%,#80848a 75%,#b5b7b9 100%)}
.front-footer{left:0;top:500px;width:496px;height:142px}
.front-cta{right:14px;top:590px;text-align:right;color:var(--blue)}
.front-cta .phone{font:300 17px/1 "Oswald",sans-serif}
.web{font-size:8.5px;color:var(--blue);margin-top:5px;display:flex;align-items:center;gap:3px;justify-content:flex-end}
.web i{display:inline-block;width:7px;height:7px;border:1.3px solid currentColor;border-radius:50%}

/* back */
.back-hero{left:0;top:0;width:496px;height:240px;background:linear-gradient(180deg,#f6f6f5 0%,#dfe1e2 60%,#c9cbcd 100%)}
.finance-panel{left:19px;top:152px;width:468px;height:352px;background:linear-gradient(180deg,var(--blue),#1a67b8)}
.finance-panel h2{color:#fff;font:300 16px/1 "Oswald",sans-serif;text-align:center;margin-top:20px}
.panel-notch{left:253px;top:502px;width:0;height:0;border-left:18px solid transparent;border-right:18px solid transparent;border-top:17px solid #1a67b8}
.cards{position:absolute;left:17px;top:47px;display:flex;gap:9px}
.card{width:133px;height:218px;background:#fff;border-radius:3px;padding:14px 8px 0 8px;color:var(--ink)}
.card h3{color:var(--blue);font:400 12px/1 "Oswald",sans-serif;text-align:center;padding-bottom:8px;border-bottom:1px solid var(--blue);margin:0 4px 10px}
.card ul{list-style:none}
.card li{position:relative;font-size:7px;line-height:1.4;padding-left:11px;margin-bottom:10px}
.card li svg{position:absolute;left:0;top:2px;width:6px;height:6px}
.panel-copy{position:absolute;left:18px;right:18px;top:290px;color:#fff;font-size:8.6px;line-height:1.4;text-align:center}
.back-bottom{left:0;top:540px;width:496px;height:102px}
.back-cta{left:0;top:535px;width:496px;text-align:center}
.back-cta h2{color:var(--blue);font:300 17px/1 "Oswald",sans-serif}
.back-cta p{font-size:7.6px;color:#666;margin-top:6px}
.pill{display:inline-block;margin-top:8px;width:214px;height:26px;border-radius:13px;background:linear-gradient(90deg,var(--blue-bright),var(--navy));color:#fff;font:300 17px/26px "Oswald",sans-serif}
.back-cta .web{justify-content:center;margin-top:6px}
</style>
</head>
<body>

<!-- Front side -->
<section class="flyer flyer--front">
  <div class="photo front-hero" role="img" aria-label="Father and young daughter laughing while baking in a bright white kitchen"></div>
  <div class="abs ribbon">Top-Rated Local Company</div>
  <div class="abs brand"><span class="brand-dot"></span>Harrowgate Home Works</div>
  <h1 class="abs title-band">KITCHEN &amp; BATH REMODELING</h1>
  <div class="abs service-band">
    <h2>HIRE A FULL-SERVICE REMODELING COMPANY</h2>
    <div class="services">
      <div class="service">
        <svg viewBox="0 0 46 46"><circle cx="23" cy="23" r="21.5" fill="none" stroke="#fff" stroke-width="1.5"/><rect x="13" y="20" width="20" height="12" fill="none" stroke="#fff" stroke-width="1.3"/><line x1="13" y1="25" x2="33" y2="25" stroke="#fff" stroke-width="1.1"/></svg>
        <h3>KITCHEN REMODELING</h3>
        <p>Hire us to create the kitchen<br>of your dreams.</p>
      </div>
      <div class="service">
        <svg viewBox="0 0 46 46"><circle cx="23" cy="23" r="21.5" fill="none" stroke="#fff" stroke-width="1.5"/><rect x="13" y="24" width="20" height="9" fill="none" stroke="#fff" stroke-width="1.3"/><circle cx="27" cy="17" r="4" fill="none" stroke="#fff" stroke-width="1.2"/></svg>
        <h3>BATHROOM REMODELING</h3>
        <p>Turn your bathroom into<br>a relaxing oasis.</p>
      </div>
      <div class="service">
        <svg viewBox="0 0 46 46"><circle cx="23" cy="23" r="21.5" fill="none" stroke="#fff" stroke-width="1.5"/><path d="M14 32V20l9-6 9 6v12z" fill="none" stroke="#fff" stroke-width="1.3"/></svg>
        <h3>HOME ADDITIONS</h3>
        <p>Renew your home by<br>expanding your space.</p>
      </div>
      <div class="service">
        <svg viewBox="0 0 46 46"><circle cx="23" cy="23" r="21.5" fill="none" stroke="#fff" stroke-width="1.5"/><line x1="12" y1="30" x2="34" y2="30" stroke="#fff" stroke-width="1.3"/><path d="M15 20h16l-8-5z" fill="none" stroke="#fff" stroke-width="1.2"/><line x1="23" y1="20" x2="23" y2="30" stroke="#fff" stroke-width="1.2"/></svg>
        <h3>DECKS/PATIOS</h3>
        <p>Work with our deck builder to create<br>a beautiful outdoor living space.</p>
      </div>
    </div>
  </div>
  <div class="photo bath-photo" role="img" aria-label="Modern bathroom with dark vanity, soaking tub and grey tiled shower"></div>
  <svg class="abs front-footer" viewBox="0 0 496 142" preserveAspectRatio="none">
    <polygon points="0,142 496,29 496,142" fill="#e9eaec"/>
    <path d="M0,78 Q70,118 140,142 L115,142 Q55,120 0,95 Z" fill="#1a6cc0"/>
    <path d="M0,96 Q60,126 110,142 L0,142 Z" fill="#0f4fa8"/>
    <path d="M0,70 Q80,112 160,142 L152,142 Q75,114 0,76 Z" fill="#ffffff"/>
  </svg>
  <div class="abs front-cta">
    <div class="phone">FREE ESTIMATE 555-014-2290</div>
    <div class="web"><i></i>www.harrowgatehomeworks.com</div>
  </div>
</section>

<!-- Back side -->
<section class="flyer flyer--back">
  <div class="photo back-hero" role="img" aria-label="Bright white kitchen with glass cabinets, flowers and pastries on a marble island"></div>
  <div class="abs finance-panel">
    <h2>READY FOR A BEAUTIFUL AND FUNCTIONAL KITCHEN OR BATHROOM?</h2>
    <div class="cards">
      <article class="card">
        <h3>HOME EQUITY LOAN</h3>
        <ul>
          <li><svg viewBox="0 0 6 6"><path d="M.5 3l1.8 1.8L5.5 1" fill="none" stroke="#1f6fc2" stroke-width="1.1"/></svg>Borrow the required sum using your home equity as collateral.</li>
          <li><svg viewBox="0 0 6 6"><path d="M.5 3l1.8 1.8L5.5 1" fill="none" stroke="#1f6fc2" stroke-width="1.1"/></svg>You get the complete amount in advance where after you cannot draw more money, and the sum must be paid off in fully authorized payments.</li>
          <li><svg viewBox="0 0 6 6"><path d="M.5 3l1.8 1.8L5.5 1" fill="none" stroke="#1f6fc2" stroke-width="1.1"/></svg>HEL offers fixed interest rates where the interest paid could be tax-deductible.</li>
        </ul>
      </article>
      <article class="card">
        <h3>MORTGAGE REFINANCING</h3>
        <ul>
          <li><svg viewBox="0 0 6 6"><path d="M.5 3l1.8 1.8L5.5 1" fill="none" stroke="#1f6fc2" stroke-width="1.1"/></svg>Great way to finance your bathroom remodel, but also to lower your interest rate and monthly payments on your existing mortgage.</li>
          <li><svg viewBox="0 0 6 6"><path d="M.5 3l1.8 1.8L5.5 1" fill="none" stroke="#1f6fc2" stroke-width="1.1"/></svg>When refinancing, the lender uses the value of your home to determine your borrowing limit.</li>
          <li><svg viewBox="0 0 6 6"><path d="M.5 3l1.8 1.8L5.5 1" fill="none" stroke="#1f6fc2" stroke-width="1.1"/></svg>Whatever amount is left after paying off your initial mortgage can be cashed out for remodeling</li>
        </ul>
      </article>
      <article class="card">
        <h3>PERSONAL LOANS</h3>
        <ul>
          <li><svg viewBox="0 0 6 6"><path d="M.5 3l1.8 1.8L5.5 1" fill="none" stroke="#1f6fc2" stroke-width="1.1"/></svg>Pay additional costs just to acquire a loan.</li>
          <li><svg viewBox="0 0 6 6"><path d="M.5 3l1.8 1.8L5.5 1" fill="none" stroke="#1f6fc2" stroke-width="1.1"/></svg>Most lenders provide the money fairly quickly; which is very helpful for a bathroom remodel.</li>
          <li><svg viewBox="0 0 6 6"><path d="M.5 3l1.8 1.8L5.5 1" fill="none" stroke="#1f6fc2" stroke-width="1.1"/></svg>Interest rate dependent on you. The higher your credit score, lower your interest rate.</li>
        </ul>
      </article>
    </div>
    <p class="panel-copy">Whether you want to modernize the look of your home or give yourself some more livable space, you want to work with a reputable local remodeling company. Harrowgate Home Works specializes in top-quality home remodeling services in Cedar Hollow, IA.</p>
  </div>
  <div class="abs panel-notch"></div>
  <svg class="abs back-bottom" viewBox="0 0 496 102" preserveAspectRatio="none">
    <path d="M0,28 Q248,140 496,28 L496,102 L0,102 Z" fill="#1a5fb4"/>
    <path d="M0,44 Q248,150 496,44 L496,102 L0,102 Z" fill="#2a8be0"/>
    <path d="M0,52 Q248,138 496,52 L496,102 L0,102 Z" fill="#ffffff"/>
  </svg>
  <div class="abs back-cta">
    <h2>READY FOR A BEAUTIFUL AND FUNCTIONAL KITCHEN OR BATHROOM?</h2>
    <p>Work with a top-rated local remodeling company in Cedar Hollow, IA</p>
    <div class="pill">FREE ESTIMATE 555-014-2290</div>
    <div class="web"><i></i>www.harrowgatehomeworks.com</div>
  </div>
</section>

</body>
</html>
```